Tallvane gym's Kids Program Flyer design

We need a flyer design for our new kids fitness program to include some details of the program and pricing points. Red/black/gray design preferable, but open to different options (the green in the logo can be changed to red). Final design should easily portray what the program is about, hours classes are offered, and pricing.

Industry/Entity Type

Fitness

```html
<!DOCTYPE html>
<html lang="en">
<head>
<meta charset="utf-8">
<title>Tallvane Kids Program Flyer</title>
<link href="https://fonts.googleapis.com/css2?family=Oswald:wght@500;600&family=Open+Sans:wght@400;600;700&family=Roboto+Condensed:wght@400;700&display=swap" rel="stylesheet">
<style>
  :root {
    --red: #e8323b;
    --red-deep: #cf262f;
    --charcoal: #3b3b3e;
    --charcoal-dark: #2f2f31;
    --paper: #ffffff;
    --row-light: #e4e4e4;
    --row-mid: #cfcfcf;
    --stage: #5a5a5c;
    --ink: #2b2b2b;
  }
  * { box-sizing: border-box; margin: 0; padding: 0; }
  html, body { width: 1200px; height: 794px; overflow: hidden; }
  body {
    background: var(--stage);
    font-family: "Open Sans", sans-serif;
    position: relative;
  }
  .page {
    position: absolute;
    top: 17px;
    width: 540px;
    height: 760px;
    overflow: hidden;
    box-shadow: 0 6px 18px rgba(0,0,0,.35);
  }
  .page-front { left: 45px; background: var(--red); }
  .page-back { left: 615px; background: var(--charcoal); }

  /* ---------- front ---------- */
  .hero {
    position: absolute; left: 26px; right: 26px; top: 26px; height: 352px;
    background: var(--paper);
    padding: 8px;
    display: grid;
    grid-template-columns: 1fr 1fr;
    grid-template-rows: 112px 112px 1fr;
    gap: 6px;
  }
  .photo { display: block; width: 100%; height: 100%; }
  .brand {
    display: flex; align-items: center; justify-content: center; gap: 8px;
  }
  .brand-dot { width: 16px; height: 16px; border-radius: 50%; background: var(--red); }
  .brand-name {
    font-family: "Oswald", sans-serif; font-weight: 600; font-size: 26px;
    color: var(--charcoal); letter-spacing: .5px;
  }
  .headline {
    background: var(--red);
    display: flex; align-items: center; justify-content: center; text-align: center;
    font-family: "Oswald", sans-serif; font-weight: 600; font-size: 24px; line-height: 1.08;
    color: var(--paper); text-transform: uppercase; padding: 6px;
  }
  .intro {
    position: absolute; left: 30px; right: 30px; top: 396px;
    color: var(--paper);
  }
  .intro h2 { font-size: 14px; font-weight: 700; margin-bottom: 6px; }
  .intro p { font-size: 11px; line-height: 1.5; margin-bottom: 8px; }
  .contact {
    position: absolute; left: 0; right: 0; bottom: 0; height: 118px;
    background: var(--charcoal);
    color: var(--paper);
    font-family: "Roboto Condensed", sans-serif;
    text-align: center;
    padding-top: 26px;
  }
  .contact-lead { font-size: 20px; }
  .contact-line { font-size: 17px; font-weight: 700; margin-top: 6px; }

  /* ---------- back ---------- */
  .back-lead {
    background: var(--red); color: var(--paper);
    height: 118px; padding: 18px 28px;
    font-size: 10.5px; line-height: 1.55;
  }
  .schedule { padding: 16px 24px 0; color: var(--paper); }
  .schedule h2 { font-size: 14px; font-weight: 700; margin-bottom: 8px; }
  .class-formats { display: grid; grid-template-columns: 1fr 1fr; gap: 18px; font-size: 9.5px; line-height: 1.5; }
  .class-formats strong { display: block; font-weight: 700; }
  .schedule-body { display: grid; grid-template-columns: 170px 1fr; gap: 14px; margin-top: 14px; align-items: start; }
  .schedule-note { font-size: 9.5px; line-height: 1.55; }
  .timetable { width: 100%; border-collapse: collapse; background: var(--paper); color: var(--ink); font-family: "Roboto Condensed", sans-serif; }
  .timetable th { background: var(--row-mid); font-size: 13px; font-weight: 700; text-transform: uppercase; padding: 5px 4px; }
  .timetable td { font-size: 12px; font-weight: 700; padding: 6px 4px; text-align: center; border-top: 1px solid var(--row-mid); }
  .timetable td:first-child { text-align: left; padding-left: 8px; }
  .memberships { margin-top: 16px; font-family: "Roboto Condensed", sans-serif; }
  .memberships h3 { color: var(--red); font-size: 19px; font-weight: 700; text-align: center; }
  .memberships-terms { color: var(--paper); font-size: 13px; text-align: center; margin: 2px 24px 6px; }
  .tier { font-size: 14px; font-weight: 700; padding: 4px 24px; }
  .tier-first { background: var(--row-light); color: var(--ink); }
  .tier-second { background: var(--row-mid); color: var(--ink); text-align: center; }
  .tier-extra { color: var(--paper); text-align: right; }
  .gallery {
    display: grid; grid-template-columns: 1fr 1fr; gap: 8px;
    padding: 8px 24px; height: 150px;
  }
  .gallery .photo { border: 3px solid var(--paper); }
  .back-contact {
    position: absolute; left: 0; right: 0; bottom: 0; height: 96px;
    background: var(--red); color: var(--paper);
    font-family: "Roboto Condensed", sans-serif; text-align: center; padding-top: 20px;
  }
</style>
</head>
<body>

<section class="page page-front">
  <div class="hero">
    <svg class="photo" role="img" aria-label="Photo of a smiling child exercising with a coach" viewBox="0 0 10 10" preserveAspectRatio="none"><defs><linearGradient id="g1" x1="0" y1="0" x2="1" y2="1"><stop offset="0" stop-color="#f1e6da"/><stop offset="1" stop-color="#cfb8a4"/></linearGradient></defs><rect width="10" height="10" fill="url(#g1)"/></svg>
    <svg class="photo" role="img" aria-label="Photo of a girl lifting small dumbbells" viewBox="0 0 10 10" preserveAspectRatio="none"><defs><linearGradient id="g2" x1="0" y1="0" x2="1" y2="1"><stop offset="0" stop-color="#e8eef2"/><stop offset="1" stop-color="#7fb7d4"/></linearGradient></defs><rect width="10" height="10" fill="url(#g2)"/></svg>
    <div class="brand"><span class="brand-dot"></span><span class="brand-name">Tallvane Kids</span></div>
    <div class="headline">It's time to<br>get fit<br>&amp; make change<br>happen!</div>
    <svg class="photo" role="img" aria-label="Photo of children stretching on exercise balls" viewBox="0 0 10 10" preserveAspectRatio="none"><defs><linearGradient id="g3" x1="0" y1="0" x2="1" y2="1"><stop offset="0" stop-color="#f3e4e8"/><stop offset="1" stop-color="#d98aa0"/></linearGradient></defs><rect width="10" height="10" fill="url(#g3)"/></svg>
    <svg class="photo" role="img" aria-label="Photo of a girl in red doing a side stretch" viewBox="0 0 10 10" preserveAspectRatio="none"><defs><linearGradient id="g4" x1="0" y1="0" x2="1" y2="1"><stop offset="0" stop-color="#dfeff0"/><stop offset="1" stop-color="#9cc9cc"/></linearGradient></defs><rect width="10" height="10" fill="url(#g4)"/></svg>
  </div>

  <div class="intro">
    <h2>What is Tallvane Kids?</h2>
    <p>Tallvane Kids is a strength and conditioning program built for children and teens. Classes are fun, safe and scaled to each age, teaching sound movement, balance and coordination while building confidence. Our coaches keep every session active, social and full of play, so kids learn to love fitness for life.</p>
    <p>Our goal is to give young athletes a strong base for any sport they choose. We want to inspire healthy habits early.</p>
  </div>

  <div class="contact">
    <p class="contact-lead">For more information, email us at</p>
    <p class="contact-line">info@tallvanekids.com | Tallvane Kids tallvanekids.com | 555.014.2270</p>
  </div>
</section>

<section class="page page-back">
  <div class="back-lead">
    Coaches walk through each of the movements we do in class. We teach proper form for functional weight training, and we want to make sure that children in a Tallvane Kids program are having fun while they learn to get and stay fit. Young bodies pick up new skills fast, and strength training is a crucial and beneficial part of growing up.
  </div>

  <div class="schedule">
    <h2>What does a typical class look like?</h2>
    <div class="class-formats">
      <p><strong>Tallvane Kids: Class Length, 45 min</strong>Warm-up · Skill practice · Workout · Game · Cool down (10 minutes)</p>
      <p><strong>Tallvane Teens: Class Length, 1 hour</strong>Warm-up · Skill and strength · Workout · Stretch and Cool down (15-20 minutes)</p>
    </div>
    <div class="schedule-body">
      <p class="schedule-note">Each class is split by age so every athlete trains with peers at a similar level. A coach can make small changes to suit a different child, and older kids who demonstrate superb skill and have the maturity may move up.</p>
      <table class="timetable">
        <thead><tr><th>Class</th><th>Age</th><th>Day</th><th>Time</th></tr></thead>
        <tbody>
          <tr><td>TV Kids Prime</td><td>3-5</td><td>M, T, Th, F</td><td>4:30-5:00 pm</td></tr>
          <tr><td>TV Kids</td><td>6-12</td><td>M, T, Th, F</td><td>5:15-6:00 pm</td></tr>
          <tr><td>TV Teens</td><td>12-17</td><td>M, T, W, Th</td><td>6:15-7:15 pm</td></tr>
        </tbody>
      </table>
    </div>
  </div>

  <div class="memberships">
    <h3>Memberships:</h3>
    <p class="memberships-terms">Unlimited use &amp; are on a month to month basis: no contracts or cancellation fees.</p>
    <p class="tier tier-first">1st membership- $100</p>
    <p class="tier tier-second">2nd membership- $80</p>
    <p class="tier tier-extra">Each additional membership- $60</p>
  </div>

  <div class="gallery">
    <svg class="photo" role="img" aria-label="Photo of children doing floor exercises on mats" viewBox="0 0 10 10" preserveAspectRatio="none"><defs><linearGradient id="g5" x1="0" y1="0" x2="1" y2="1"><stop offset="0" stop-color="#f4ece6"/><stop offset="1" stop-color="#d9a38f"/></linearGradient></defs><rect width="10" height="10" fill="url(#g5)"/></svg>
    <svg class="photo" role="img" aria-label="Photo of a girl stretching in a bright gym" viewBox="0 0 10 10" preserveAspectRatio="none"><defs><linearGradient id="g6" x1="0" y1="0" x2="1" y2="1"><stop offset="0" stop-color="#e6f2f3"/><stop offset="1" stop-color="#86bfc6"/></linearGradient></defs><rect width="10" height="10" fill="url(#g6)"/></svg>
  </div>

  <div class="back-contact">
    <p class="contact-lead">For more information, email us at</p>
    <p class="contact-line">info@tallvanekids.com | Tallvane Kids tallvanekids.com | 555.014.2270</p>
  </div>
</section>

</body>
</html>
```